Chatterloop Now Hiring Post - Automotive Mechanics

1080 x 1080 design Chatterloop ad post that we are hiring. Text to include:

We are hiring mechanics to perform suspension, brake, clutch and steering repairs on heavy duty trucks, trailers, busses and motorhomes.
Hourly wages plus performance bonus
Harbor Wellness Alliance Heath Care + Dental
401K + Company Match
Weekly Pay
3:00 pm – 11:00 pm Shift – No Weekends
Stop in anytime at Oakridge Axle Works 2718 Heron Lane, Saginaw, MI 48602
or call 989-412-7730
email you resume to axleworks@axleworks.example

Target Market(s)

Automotive mechanics / Technicians

Industry/Entity Type

Automotive

Font styles to use
Sans Serif

Colors
0054AA
0677BA
7BADD7
CADEEF
E8F1F8

Requirements
Must have
• Must include the text, our logo, and picture from our service department file = oakridge-axle-works-service.jpg
Nice to have
• Something similar to the same Pintor Motors repair ad I attached
Should not have
• No images of people. The image that we provided is from our repair shop, we would like that one used.

```html
<!DOCTYPE html>
<html lang="en">
<head>
<meta charset="utf-8">
<title>Oakridge Axle Works – We Are Hiring</title>
<link rel="stylesheet" href="https://fonts.googleapis.com/css2?family=Lexend:wght@400;500;600;700&family=Poppins:wght@800;900&display=swap">
<style>
  :root {
    --blue-deep: #0054AA;
    --blue-mid: #0677BA;
    --blue-soft: #7BADD7;
    --blue-pale: #CADEEF;
    --blue-mist: #E8F1F8;
    --navy: #0a1628;
    --navy-2: #14263f;
    --ink-blue: #1a4f9c;
    --white: #ffffff;
  }
  * { margin: 0; padding: 0; box-sizing: border-box; }
  html, body { width: 1200px; height: 1200px; overflow: hidden; background: var(--navy); }
  .poster {
    position: relative; width: 1200px; height: 1200px; overflow: hidden;
    font-family: "Lexend", sans-serif; color: var(--white);
    background: var(--navy);
  }
  .shop-photo {
    position: absolute; left: 0; top: 0; width: 1200px; height: 970px;
    background:
      radial-gradient(ellipse 260px 200px at 1080px 430px, #6f6a66 0%, #4e4c4d 45%, transparent 100%),
      radial-gradient(ellipse 230px 330px at 830px 560px, #2f4f8a 0%, #24406f 45%, transparent 100%),
      radial-gradient(ellipse 420px 130px at 860px 830px, #c9d0d8 0%, #7d8fa8 45%, transparent 100%),
      radial-gradient(ellipse 480px 260px at 900px 230px, #55504d 0%, #3a3b40 55%, transparent 100%),
      linear-gradient(90deg, #0b1628 0%, #13233a 38%, #2b3647 62%, #3c4352 100%);
  }
  .shop-photo-fade {
    position: absolute; left: 0; top: 0; width: 720px; height: 970px;
    background: linear-gradient(90deg, rgba(10,22,40,0.95) 0%, rgba(10,22,40,0.75) 60%, rgba(10,22,40,0) 100%);
  }
  .brand-tab { position: absolute; left: 0; top: 0; width: 1200px; height: 132px; }
  .brand {
    position: absolute; top: 30px; left: 0; width: 1200px;
    display: flex; justify-content: center; align-items: center; gap: 20px;
  }
  .brand-square { width: 62px; height: 62px; background: var(--blue-deep); flex: none; }
  .brand-name {
    font-family: "Lexend", sans-serif; font-weight: 700; font-size: 46px;
    color: var(--blue-deep); line-height: 56px; letter-spacing: 0.5px;
  }
  .headline-top {
    position: absolute; left: 166px; top: 214px;
    font-family: "Poppins", sans-serif; font-weight: 800; font-size: 82px; line-height: 1;
    letter-spacing: -1px;
  }
  .headline-box { position: absolute; left: 38px; top: 298px; width: 585px; height: 131px; }
  .headline-main {
    position: absolute; left: 68px; top: 288px;
    font-family: "Poppins", sans-serif; font-weight: 800; font-size: 128px; line-height: 150px;
    letter-spacing: -3px;
  }
  .intro {
    position: absolute; left: 38px; top: 430px; width: 640px;
    font-size: 31px; font-weight: 500; line-height: 40px;
  }
  .benefits { position: absolute; left: 40px; top: 600px; list-style: none; }
  .benefit { position: absolute; left: 0; width: 520px; height: 56px; }
  .benefit svg { position: absolute; left: 0; width: 48px; height: 52px; }
  .benefit span {
    position: absolute; left: 74px; top: 0; font-size: 22px; font-weight: 500; line-height: 28px; white-space: nowrap;
  }
  .contact-band { position: absolute; left: 0; top: 970px; width: 1200px; height: 178px; background: var(--white); }
  .footer-strip { position: absolute; left: 0; top: 1148px; width: 1200px; height: 52px; background: linear-gradient(180deg, #1b2230, #0d121b); }
  .visit-panel { position: absolute; left: 0; top: 986px; width: 505px; height: 162px; }
  .visit-lead { position: absolute; left: 91px; top: 1010px; font-size: 24px; font-weight: 500; line-height: 26px; }
  .visit-name { position: absolute; left: 91px; top: 1034px; font-size: 29px; font-weight: 700; line-height: 30px; }
  .visit-address { position: absolute; left: 91px; top: 1086px; font-size: 24px; font-weight: 400; line-height: 26px; width: 380px; }
  .pin-icon { position: absolute; left: 29px; top: 1084px; width: 36px; height: 50px; }
  .contact-line { position: absolute; left: 663px; color: var(--ink-blue); line-height: 32px; }
  .contact-email { top: 1007px; font-size: 27px; font-weight: 500; }
  .contact-phone { top: 1081px; font-size: 29px; font-weight: 600; }
  .contact-icon { position: absolute; left: 585px; width: 52px; height: 54px; }
</style>
</head>
<body>
<main class="poster">
  <div class="shop-photo" role="img" aria-label="Photo from the service department: heavy duty truck brake and hub assembly in a repair bay, with a bus, a semi truck and a motorhome parked in front"></div>
  <div class="shop-photo-fade" aria-hidden="true"></div>

  <svg class="brand-tab" viewBox="0 0 1200 132" aria-hidden="true">
    <path d="M40 0 L205 108 Q230 130 260 130 L940 130 Q970 130 995 108 L1160 0 Z" fill="var(--white)"/>
    <path d="M40 0 L205 108" stroke="var(--blue-deep)" stroke-width="5" fill="none"/>
    <path d="M1160 0 L995 108" stroke="var(--blue-deep)" stroke-width="5" fill="none"/>
  </svg>
  <div class="brand">
    <span class="brand-square" aria-hidden="true"></span>
    <span class="brand-name">Oakridge Axle Works</span>
  </div>

  <h1>
    <span class="headline-top">WE ARE</span>
    <svg class="headline-box" viewBox="0 0 585 131" aria-hidden="true">
      <defs>
        <linearGradient id="hiringFill" x1="0" x2="1">
          <stop offset="0" stop-color="#10407e"/>
          <stop offset="1" stop-color="var(--blue-mid)"/>
        </linearGradient>
      </defs>
      <path d="M28 0 L585 0 L572 110 Q569 131 548 131 L0 131 L10 20 Q13 0 28 0 Z" fill="url(#hiringFill)"/>
    </svg>
    <span class="headline-main">HIRING!</span>
  </h1>

  <p class="intro">we are hiring mechanics to perform suspension, brake, clutch and steering repairs on heavy duty trucks, trailers, busses and motorhomes.</p>

  <ul class="benefits">
    <li class="benefit" style="top:1px">
      <svg style="top:2px" viewBox="0 0 48 52" aria-hidden="true"><g fill="none" stroke="var(--blue-mid)" stroke-width="3"><rect x="2" y="12" width="36" height="24" rx="3"/><path d="M6 40h36V18M10 44h36V22"/></g><text x="20" y="31" font-family="Lexend" font-weight="700" font-size="18" fill="var(--blue-mid)" text-anchor="middle">$</text></svg>
      <span>Hourly wages plus<br>performance bonus</span>
    </li>
    <li class="benefit" style="top:85px">
      <svg style="top:0" viewBox="0 0 48 52" aria-hidden="true"><path d="M24 2 L44 9 V26 Q44 42 24 50 Q4 42 4 26 V9 Z" fill="var(--blue-deep)"/><path d="M20 16h8v6h6v8h-6v6h-8v-6h-6v-8h6z" fill="var(--navy)"/></svg>
      <span>Harbor Wellness Alliance<br>Heath Care + Dental</span>
    </li>
    <li class="benefit" style="top:167px">
      <svg style="top:-18px" viewBox="0 0 48 52" aria-hidden="true"><g fill="var(--blue-deep)"><rect x="4" y="38" width="7" height="12"/><rect x="14" y="32" width="7" height="18"/><rect x="24" y="26" width="7" height="24"/><rect x="34" y="18" width="7" height="32"/></g><path d="M4 30 L20 20 L28 24 L42 6" stroke="var(--blue-deep)" stroke-width="3" fill="none"/><path d="M34 5 L44 3 L43 13 Z" fill="var(--blue-deep)"/></svg>
      <span>401K + Company Match</span>
    </li>
    <li class="benefit" style="top:223px">
      <svg style="top:-9px" viewBox="0 0 48 52" aria-hidden="true"><g fill="none" stroke="var(--blue-deep)" stroke-width="3"><rect x="3" y="8" width="36" height="34" rx="3"/><path d="M3 18h36M12 3v9M30 3v9"/></g><circle cx="38" cy="40" r="10" fill="var(--blue-deep)"/><text x="38" y="45" font-family="Lexend" font-weight="700" font-size="13" fill="var(--navy)" text-anchor="middle">$</text></svg>
      <span>Weekly Pay</span>
    </li>
    <li class="benefit" style="top:278px">
      <svg style="top:2px" viewBox="0 0 48 52" aria-hidden="true"><circle cx="24" cy="28" r="20" fill="none" stroke="var(--blue-deep)" stroke-width="3"/><path d="M24 14v14l-8 6" stroke="var(--blue-deep)" stroke-width="3" fill="none"/></svg>
      <span>3:00 pm - 11:00 pm Shift<br>No Weekends</span>
    </li>
  </ul>

  <div class="contact-band"></div>
  <div class="footer-strip"></div>

  <svg class="visit-panel" viewBox="0 0 505 162" aria-hidden="true">
    <defs>
      <linearGradient id="visitFill" x1="0" x2="1">
        <stop offset="0" stop-color="#0f3f7c"/>
        <stop offset="1" stop-color="var(--blue-mid)"/>
      </linearGradient>
    </defs>
    <path d="M0 70 L40 10 Q47 2 60 2 L440 2 Q453 2 458 14 L505 162 L0 162 Z" fill="url(#visitFill)"/>
  </svg>
  <svg class="pin-icon" viewBox="0 0 36 50" aria-hidden="true"><path d="M18 2 C8 2 2 9 2 18 C2 30 18 48 18 48 C18 48 34 30 34 18 C34 9 28 2 18 2 Z" fill="var(--white)"/><circle cx="18" cy="18" r="6" fill="var(--blue-deep)"/></svg>
  <p class="visit-lead">STOP IN ANYTIME AT</p>
  <p class="visit-name">Oakridge Axle Works</p>
  <p class="visit-address">2718 Heron Lane, Saginaw, MI 48602</p>

  <svg class="contact-icon" style="top:995px" viewBox="0 0 52 54" aria-hidden="true"><g fill="none" stroke="var(--ink-blue)" stroke-width="3"><rect x="3" y="20" width="46" height="31" rx="4"/><path d="M4 22 L26 40 L48 22M4 50 L20 36M48 50 L32 36"/></g><path d="M21 2h10v12h7L26 26 14 14h7z" fill="var(--ink-blue)"/></svg>
  <p class="contact-line contact-email">axleworks@axleworks.example</p>

  <svg class="contact-icon" style="top:1068px" viewBox="0 0 52 54" aria-hidden="true"><path d="M10 8 L18 6 L22 18 L16 22 Q20 32 30 38 L34 32 L46 36 L44 44 Q40 52 30 48 Q10 38 4 18 Q4 10 10 8 Z" fill="var(--ink-blue)"/><g fill="none" stroke="var(--ink-blue)" stroke-width="2.5"><path d="M30 14 Q36 16 38 22"/><path d="M32 6 Q44 10 46 22"/></g></svg>
  <p class="contact-line contact-phone">989-412-7730</p>
</main>
</body>
</html>
```